Swim school needs flyer design

Need revamp of flyer design. Attached last years flyer (BCP A4 Holiday Leaflet-v6.2 (1)). Also attached is this years information in word format (BCP A4 BCP & Holiday Leaflet 2014-2015).
This flyer must fit with our logo (Blue Current Pools-RGB). This flyer is our first point of call for many of our clients. With the amount of information that must be provided, it is important that it flows and is appealing. Photos can be accessed from http://kemapics.brightfolio.net/apps/photos/album?albumid=52930417 or from your own source
Important that the final design fits printers template.(Flyers-A4-210x297mm-2Side - attached)

```html
<!DOCTYPE html>
<html lang="en">
<head>
<meta charset="utf-8">
<title>Blue Current Pools – Holiday Swim Classes</title>
<link rel="stylesheet" href="https://fonts.googleapis.com/css2?family=Bitter:wght@700;800&family=Open+Sans:wght@400;600;700;800&display=swap">
<style>
:root{
  --page:#eef1f4;
  --white:#ffffff;
  --navy:#2a4c9c;
  --blue:#1e9ad6;
  --blue-deep:#0f6fb0;
  --yellow:#ffd21c;
  --gold:#f4b82a;
  --green:#9ac53c;
  --orange:#f28a1e;
  --red:#e5202b;
  --maroon:#8c1b3a;
  --brown:#7a4a2b;
  --paper:#efe6cc;
  --ink:#1f2a3a;
  --rule:#9aa3ad;
}
*{box-sizing:border-box;margin:0;padding:0}
html,body{width:1040px;height:1200px;overflow:hidden}
body{background:var(--page);font-family:"Open Sans",sans-serif;color:var(--ink)}
.flyer{position:absolute;left:130px;top:85px;width:780px;height:1030px;background:var(--white);overflow:hidden;box-shadow:0 6px 24px rgba(0,0,0,.18)}
.abs{position:absolute}
.hero-photo{left:0;top:0;width:780px;height:340px;background:linear-gradient(120deg,#cfe9f6 0%,#7cc4e8 40%,#4aa6d8 70%,#9bd6f1 100%)}
.waves{left:0;top:0;width:780px;height:700px}
.yellow-panel{left:40px;top:380px;width:330px;height:310px;background:var(--yellow)}
.contact-top{left:305px;top:14px}
.contact-top .phone{font-weight:700;color:var(--navy);font-size:24px;letter-spacing:.5px}
.contact-top .web{font-size:11px;color:var(--navy);font-weight:600}
.brand{left:510px;top:92px;display:flex;align-items:center;gap:10px;white-space:nowrap}
.brand .dot{width:20px;height:20px;border-radius:50%;background:var(--orange)}
.brand .name{font-weight:700;font-size:24px;color:var(--blue-deep)}
.sign{left:402px;top:292px;width:300px;height:160px;background:var(--white);border:8px solid var(--gold);transform:rotate(-2deg);display:flex;align-items:center;justify-content:center;text-align:center;box-shadow:2px 4px 8px rgba(0,0,0,.25)}
.sign h1{font-family:"Bitter",serif;font-weight:800;color:var(--navy);font-size:40px;line-height:1.05}
.sign h1 span{font-size:36px;display:block}
.dates-ribbon{left:28px;top:445px;width:290px;height:50px;background:linear-gradient(var(--blue),var(--blue-deep));border-radius:8px 26px 26px 8px;color:var(--white);font-weight:700;font-size:20px;display:flex;align-items:center;padding-left:24px;box-shadow:0 3px 0 #0b4e7d}
.dates{top:506px;width:155px}
.dates h3{color:var(--red);font-weight:800;font-size:20px;text-align:center;line-height:26px}
.dates ul{list-style:none}
.dates li{color:var(--navy);font-weight:700;font-size:15px;line-height:26px;white-space:nowrap;letter-spacing:-.2px}
.dates-2014{left:52px}
.dates-2015{left:210px}
.dates-note{left:150px;top:640px;font-size:9px;color:var(--ink)}
.price-card{left:382px;top:498px;width:150px;height:165px;background:var(--paper);transform:rotate(12deg);padding:52px 8px 0 18px;color:var(--red);font-weight:800;line-height:1.1;box-shadow:2px 3px 6px rgba(0,0,0,.25)}
.price-card p{margin-bottom:6px}
.price-card .big{font-size:20px}
.price-card .sm{font-size:14px}
.special-tag{left:432px;top:408px;width:54px;height:125px;background:var(--brown);border-radius:27px 27px 6px 6px;transform:rotate(-16deg);color:var(--paper);font-weight:700;font-size:12px;display:flex;flex-direction:column;align-items:center;justify-content:flex-end;padding-bottom:8px;line-height:13px}
.special-tag::before{content:"";width:11px;height:11px;border-radius:50%;background:var(--paper);position:absolute;top:11px}
.info-band{left:0;top:690px;width:780px;height:205px;background:linear-gradient(90deg,var(--blue-deep),var(--blue) 55%,#56bde9)}
.important{left:88px;top:668px;width:160px;height:34px;background:var(--maroon);color:var(--white);font-weight:700;font-size:19px;display:flex;align-items:center;justify-content:center;border-radius:4px 14px 14px 4px}
.notes{top:718px;list-style:none;color:var(--white);font-size:13.5px;line-height:18px}
.notes li{position:relative;padding-left:28px;margin-bottom:12px}
.notes li::before{content:"";position:absolute;left:2px;top:3px;width:13px;height:13px;background:var(--gold);transform:rotate(45deg);border-radius:2px}
.notes-left{left:42px;width:245px}
.notes-right{left:300px;width:220px}
.polaroid{background:var(--white);padding:9px;box-shadow:2px 4px 10px rgba(0,0,0,.3)}
.polaroid .ph{width:100%;height:100%}
.polaroid-1{left:552px;top:440px;width:185px;height:155px;transform:rotate(6deg)}
.polaroid-2{left:530px;top:590px;width:200px;height:160px;transform:rotate(-7deg)}
.polaroid-3{left:565px;top:740px;width:180px;height:150px;transform:rotate(3deg);background:var(--yellow)}
.ph-1{background:linear-gradient(135deg,#5bc3e6,#2a8fc6)}
.ph-2{background:linear-gradient(135deg,#7fd0f0,#f3c6b3 60%,#3aa0d6)}
.ph-3{background:linear-gradient(135deg,#2f8fd0,#88d2f0 60%,#1d6fb3)}
.band-line{left:0;top:886px}
.contacts-title{left:42px;top:912px;color:var(--blue);font-weight:700;font-size:16px}
.contact-col{top:937px;font-size:9px;line-height:1.4;color:var(--ink);white-space:nowrap}
.contact-col strong{display:block;font-size:10px}
.col-1{left:42px;width:170px}
.col-2{left:214px;width:130px;border-left:1px solid var(--rule);padding-left:8px}
.col-3{left:348px;width:160px;border-left:1px solid var(--rule);padding-left:8px}
.contact-big{left:520px;top:945px;color:var(--navy);font-weight:800}
.contact-big .phone{font-size:28px;line-height:1}
.contact-big .web{font-size:14.5px;font-weight:700;margin-top:3px}
.footer-bar{left:0;top:1003px;width:780px;height:27px;background:var(--green);color:var(--navy);font-size:9.5px;font-weight:600;display:flex;align-items:center;justify-content:center}
</style>
</head>
<body>
<main class="flyer">
  <div class="abs hero-photo" role="img" aria-label="Photo of a child in goggles swimming freestyle in a pool"></div>

  <svg class="abs waves" viewBox="0 0 780 700" aria-hidden="true">
    <path d="M280 0 H780 V210 C700 200 640 170 600 120 C560 70 420 60 300 40 Z" fill="#ffffff"/>
    <path d="M470 150 C520 20 700 -10 780 40" fill="none" stroke="#1e9ad6" stroke-width="6"/>
    <path d="M450 165 C500 60 660 10 780 70" fill="none" stroke="#f28a1e" stroke-width="4"/>
    <path d="M0 300 C150 250 250 340 420 300 C560 265 680 250 780 280 V700 H0 Z" fill="#9ac53c"/>
    <path d="M0 270 C120 360 260 300 380 330 C470 350 560 300 600 290 L600 310 C520 330 460 370 360 360 C240 350 120 390 0 320 Z" fill="#1e9ad6"/>
    <path d="M0 255 C140 330 250 290 330 300 C260 310 160 350 0 290 Z" fill="#ffd21c"/>
    <path d="M0 300 C200 320 300 340 400 340 C500 340 640 300 780 330" fill="none" stroke="#f28a1e" stroke-width="5"/>
    <path d="M520 240 L540 262 M560 230 L540 262" stroke="#7a4a2b" stroke-width="2"/>
    <circle cx="540" cy="262" r="4" fill="#7a4a2b"/>
  </svg>

  <div class="abs yellow-panel"></div>

  <div class="abs contact-top">
    <div class="phone">(03) 9000 4821</div>
    <div class="web">www.bluecurrentpools.com.au</div>
  </div>

  <div class="abs brand">
    <span class="dot"></span>
    <span class="name">Blue Current Pools</span>
  </div>

  <div class="abs sign"><h1>Holiday<span>Swim</span>Classes</h1></div>

  <div class="abs dates-ribbon">Holiday Program Dates</div>

  <div class="abs dates dates-2014">
    <h3>2014</h3>
    <ul><li>Sep 23rd - 27th</li><li>Sep 30th - Oct 4th</li><li>Jan 6th &nbsp;&nbsp;- 10th</li><li>Jan 13th &nbsp;- 17th</li></ul>
  </div>
  <div class="abs dates dates-2015">
    <h3>2015</h3>
    <ul><li>Sep 23rd - 27th</li><li>Sep 30th - Oct 4th</li><li>Jan 6th &nbsp;&nbsp;- 10th</li><li>Jan 13th &nbsp;- 17th</li></ul>
  </div>
  <div class="abs dates-note">* $52 per child due to 4 day week</div>

  <div class="abs price-card">
    <p><span class="big">$75</span> <span class="sm">per child per week</span></p>
    <p><span class="big">5x½</span> <span class="sm">hour classes per week</span></p>
  </div>
  <div class="abs special-tag"><span>S</span><span>P</span><span>E</span><span>C</span><span>I</span><span>A</span><span>L</span></div>

  <div class="abs info-band"></div>
  <div class="abs important">Important</div>
  <ul class="abs notes notes-left">
    <li>All holiday swim classes are conducted at the Northvale primary school pool</li>
    <li>30 minute classes run every ½ hour from 9.30am to 12 noon</li>
    <li>Limited places due to small class sizes</li>
  </ul>
  <ul class="abs notes notes-right">
    <li>Beginners to advanced swimmers welcome</li>
    <li>All children are grouped by age and ability</li>
    <li>No refunds or makeups for holiday programs</li>
  </ul>

  <svg class="abs band-line" width="780" height="20" viewBox="0 0 780 20" aria-hidden="true">
    <path d="M0 6 C200 18 500 0 780 10" fill="none" stroke="#f28a1e" stroke-width="4"/>
  </svg>

  <div class="abs polaroid polaroid-1"><div class="ph ph-1" role="img" aria-label="Photo of a child swimming underwater with a kickboard"></div></div>
  <div class="abs polaroid polaroid-2"><div class="ph ph-2" role="img" aria-label="Photo of a parent and toddler in swim caps in the pool"></div></div>
  <div class="abs polaroid polaroid-3"><div class="ph ph-3" role="img" aria-label="Photo of a young child in a red cap swimming underwater"></div></div>

  <div class="abs contacts-title">Pool Locations Contact Details &amp; Office Hours</div>
  <div class="abs contact-col col-1"><strong>Northvale P.S. Pool</strong>Location: 42 Reed Street,<br>Northvale 3190, Ph: 9000 4821<br>Office Hours: Mon-Fri 9:00am-5:30pm,<br>Sat-Sun 9.15am-12.15pm</div>
  <div class="abs contact-col col-2"><strong>Elmwood College Pool</strong>Location: Gate 2,<br>Ferris Road,<br>Elmwood 3191</div>
  <div class="abs contact-col col-3"><strong>All Correspondence</strong>Post: P.O. Box 5120,<br>Elmwood 3191<br>ABN: 00 123 456 789<br>Email: info@bluecurrentpools.com.au</div>

  <div class="abs contact-big">
    <div class="phone">(03) 9000 4821</div>
    <div class="web">www.bluecurrentpools.com.au</div>
  </div>

  <div class="abs footer-bar">Our qualified staff makes swimming not only a rewarding but also a lot of fun. This is a great opportunity to kick-start your child's aquatic education.</div>
</main>
</body>
</html>
```